Business Card Design Project

New Private residential substance abuse treatment facility in Mapleton, UT. Facility located in elegant 11,000 home with stunning views of the mountains. Wish to incorporate colored logo. Business name- Birchwell Harbor Wellness. Facility is Tudor style with traditional furnishings, an overhead picture is attached. Lettering in a simple scroll or old english style. Must be easy to read with clear moderetly large font.
Updates

It seems the project time frame listed was not correct- it is a week.

Target Market(s)

Adults 18 and over with substance abuse issues requiring residential rehabilitation. Referral base are medical/mental health professionals, families and community agencies.

Industry/Entity Type

Residential

Colors
9bcb3b
fece3e
fbee3f

Requirements
Must have
• Clear and easy to read, professional and upscale presentation. Need logo, name, title, address, phone, fax and web page address. May add slogan later. Use same font as logo.
Nice to have
• Logo has a green mountain and a gold maple leaf so a nature themed element may work. Want to promote peaceful grounded image. Logo attached.
Should not have
• No tiny or complicated font. No modern or tech looking images. No light colored fonts.

```html
<!DOCTYPE html>
<html lang="en">
<head>
<meta charset="utf-8">
<title>Birchwell Harbor Wellness — Business Card</title>
<link rel="stylesheet" href="https://fonts.googleapis.com/css2?family=Josefin+Sans:wght@400;600&display=swap">
<style>
  :root {
    --card-green: #9bcb3b;
    --ink: #3a4526;
    --accent-gold: #fece3e;
    --accent-yellow: #fbee3f;
    --rule: #6f8f2a;
  }
  * { margin: 0; padding: 0; box-sizing: border-box; }
  html, body { width: 1200px; height: 705px; overflow: hidden; }
  body { background: var(--card-green); font-family: "Josefin Sans", Arial, sans-serif; color: var(--ink); }
  .card { position: relative; width: 1200px; height: 705px; background: var(--card-green); }

  .brand {
    position: absolute; left: 150px; top: 300px; width: 520px;
    display: flex; align-items: center; gap: 22px;
  }
  .brand-mark { width: 54px; height: 54px; border-radius: 50%; background: var(--accent-gold); flex: none; }
  .brand-name { font-weight: 600; color: var(--ink); line-height: 1.05; }
  .brand-name .primary { display: block; font-size: 46px; }
  .brand-name .secondary { display: block; font-size: 20px; letter-spacing: 8px; margin-top: 8px; }

  .contact {
    position: absolute; left: 690px; top: 205px;
    display: grid; grid-template-columns: 36px 1px auto; column-gap: 22px;
  }
  .contact-icons, .contact-lines { display: flex; flex-direction: column; }
  .contact-icons svg { width: 26px; height: 26px; margin: 7px 0 11px; fill: var(--accent-gold); }
  .contact-rule { background: var(--rule); }
  .contact-lines li {
    list-style: none; height: 44px; line-height: 44px;
    font-size: 21px; letter-spacing: 2.5px; text-transform: uppercase;
  }
</style>
</head>
<body>
<main class="card">
  <div class="brand">
    <span class="brand-mark" aria-hidden="true"></span>
    <h1 class="brand-name">
      <span class="primary">Birchwell Harbor</span>
      <span class="secondary">WELLNESS</span>
    </h1>
  </div>

  <section class="contact" aria-label="Contact details">
    <div class="contact-icons" aria-hidden="true">
      <svg viewBox="0 0 24 24"><path d="M12 3 2 12h3v9h5v-6h4v6h5v-9h3z"/></svg>
      <svg viewBox="0 0 24 24"><path d="M7 2h10a1 1 0 0 1 1 1v18a1 1 0 0 1-1 1H7a1 1 0 0 1-1-1V3a1 1 0 0 1 1-1zm1 3v13h8V5zm4 14.2a1 1 0 1 0 0 2 1 1 0 0 0 0-2z"/></svg>
      <svg viewBox="0 0 24 24"><path d="M6.6 10.8a15 15 0 0 0 6.6 6.6l2.2-2.2a1 1 0 0 1 1-.25 11 11 0 0 0 3.6.6 1 1 0 0 1 1 1V20a1 1 0 0 1-1 1A17 17 0 0 1 3 4a1 1 0 0 1 1-1h3.5a1 1 0 0 1 1 1 11 11 0 0 0 .6 3.6 1 1 0 0 1-.25 1z"/></svg>
      <svg viewBox="0 0 24 24"><circle cx="12" cy="12" r="11"/><path fill="#9bcb3b" d="M8 6h8v3H8zm-2 4h12v6h-2v-2H8v2H6zm2 5h8v3H8z"/></svg>
      <svg viewBox="0 0 24 24"><circle cx="12" cy="12" r="11"/><path fill="#9bcb3b" d="M6 8h12v8H6zm1 1v.4l5 3.3 5-3.3V9z"/></svg>
      <svg viewBox="0 0 24 24"><circle cx="12" cy="12" r="11"/><path fill="none" stroke="#9bcb3b" stroke-width="1.6" d="M5 12h14M12 4.5c-4 4.5-4 10.5 0 15M12 4.5c4 4.5 4 10.5 0 15"/></svg>
    </div>
    <div class="contact-rule"></div>
    <ul class="contact-lines">
      <li>Adress</li>
      <li>012-345-678</li>
      <li>012-345-678</li>
      <li>012-345-678</li>
      <li>email@site.com</li>
      <li>website.com</li>
    </ul>
  </section>
</main>
</body>
</html>
```